Sales Flyer or Trifold for selling our Monthly Computer Service

I need a flyer designed for our new monthly computer maintenance service. We have been using this software package for 3 years for business customers with much success, but now we want to sell this to individual residential clients with the idea that we can keep their computer safe, running well, and less of a hassle for them. It also will create a steady work load for my technicians, and stable recurring income.

I tried making something, but it is too amateur looking. The final design should look professional, be engaging, and draw from our existing web design, logos, business cards and such. Most importantly, it should make them see value in spending $29 per month to be part of the program. I will upload as much examples of other branding as I can to give you something to go off of. We try to use open sans for text. You should also visit brightowlsupport.example for our current design scheme. I anticipate that we may go through a few revisions on this, and that I will probably have other similar signage created with complimentary designs later.

Target Market(s)

My target market is local affluent residential customers in the middle aged and up age range. People who may be or have been used to having tech support at their office.

Industry/Entity Type

Computer Repair

Font styles to use
Sans Serif

Requirements
Must have
• mention the components of the service that we offer. my existing flyer shows all of those. we also must use the logo in some way. It should have our contact information on the flyer too.
Nice to have
• I'm not sure yet, I really can't picture what I want. I am thinking a trifold. Maybe a single pager...
Should not have
• Please, please, no people with headsets on in a call center, no horrible stock imagery. We are trying to show that we are NOT a faceless call center, but instead give off a feeling of personalized support. We want to be their tech guy. Also, please do not use words with negative connotations like 'service plan' or similar. There are a lot of scammers out there claiming to do something similar and we need to disassociate ourselves as much as we can from them.

```html
<!DOCTYPE html>
<html lang="en">
<head>
<meta charset="utf-8">
<title>Night Watch – Computer Protection and Security for Your Home</title>
<link href="https://fonts.googleapis.com/css2?family=Lato:wght@300;400;700;900&display=swap" rel="stylesheet">
<style>
  :root {
    --brand-red: #c01f26;
    --ink: #1a1a1a;
    --body-ink: #2b2b2b;
    --quote-bg: #424143;
    --paper: #ffffff;
    --backdrop: #9a9a9a;
    --photo-light: #d6d6d6;
    --photo-mid: #8f8f8f;
    --photo-dark: #4a4a4a;
  }
  * { box-sizing: border-box; margin: 0; padding: 0; }
  html, body { width: 1200px; height: 1200px; overflow: hidden; }
  body {
    background: var(--backdrop);
    font-family: "Lato", sans-serif;
    position: relative;
  }
  .flyer {
    position: absolute;
    left: 160px; top: 30px;
    width: 881px; height: 1140px;
    background: var(--paper);
    overflow: hidden;
  }
  .hero {
    position: absolute; left: 0; top: 0;
    width: 881px; height: 407px;
  }
  .hero-photo {
    position: absolute; inset: 0;
    background:
      radial-gradient(ellipse 260px 200px at 260px 230px, var(--photo-light), transparent 70%),
      linear-gradient(100deg, var(--photo-dark) 0%, var(--photo-mid) 35%, var(--photo-light) 65%, var(--photo-mid) 100%);
  }
  .brand-ring {
    position: absolute; left: 576px; top: 25px;
    width: 220px; height: 220px;
    border: 6px solid var(--brand-red);
    border-radius: 50%;
  }
  .brand-name {
    position: absolute; right: 40px; top: 255px;
    font-size: 51px; font-weight: 400; letter-spacing: 1px;
    color: var(--ink); line-height: 1;
  }
  .tagline {
    position: absolute; right: 40px; top: 313px;
    text-align: right;
    font-size: 25px; font-weight: 900; line-height: 27px;
    color: var(--ink);
  }
  .features {
    position: absolute; left: 0; top: 407px;
    width: 881px; height: 236px;
    background: var(--brand-red);
  }
  .feature {
    position: absolute; top: 28px; width: 180px;
    text-align: center; color: var(--paper);
  }
  .feature svg { display: block; margin: 0 auto; height: 74px; }
  .feature-label {
    margin-top: 22px;
    font-size: 17.5px; line-height: 17.5px; font-weight: 400;
    letter-spacing: 0.4px;
    text-transform: uppercase;
  }
  .testimonial {
    position: absolute; left: 15px; top: 658px;
    width: 360px; height: 358px;
    background: var(--quote-bg);
    border-radius: 8px;
    padding: 18px 12px 0 19px;
    color: #f2f2f2;
    font-size: 19px; line-height: 26px; font-weight: 400; letter-spacing: 0.6px;
  }
  .testimonial p + p { margin-top: 26px; }
  .testimonial-tail { position: absolute; left: 40px; top: 1012px; }
  .pitch {
    position: absolute; left: 390px; top: 667px; width: 478px;
    color: var(--body-ink);
    font-size: 19px; line-height: 26px; font-weight: 400; letter-spacing: 0.6px;
  }
  .pitch p + p { margin-top: 26px; }
  .cta {
    position: absolute; left: 389px; top: 930px; width: 440px;
    color: var(--ink);
    font-size: 25px; line-height: 26px; letter-spacing: 1.8px; font-weight: 400;
  }
  .cta-lead { font-size: 34px; letter-spacing: 1.5px; }
  .contact {
    position: absolute; left: 0; top: 1090px; width: 881px;
    text-align: center;
    font-size: 20px; font-weight: 400; letter-spacing: 5px;
    color: var(--ink);
  }
</style>
</head>
<body>
<main class="flyer">
  <header class="hero">
    <div class="hero-photo" role="img" aria-label="Black and white photo of a small shaggy dog sitting beside a person typing on a laptop in a bright room"></div>
    <div class="brand-ring" aria-hidden="true"></div>
    <h1 class="brand-name">NIGHT WATCH</h1>
    <p class="tagline">COMPUTER PROTECTION AND SECURITY<br>FOR YOUR HOME</p>
  </header>

  <section class="features">
    <div class="feature" style="left:16px">
      <svg viewBox="0 0 60 80" width="56" aria-hidden="true">
        <path d="M16 34 V22 a14 14 0 0 1 28 0 V34" fill="none" stroke="#fff" stroke-width="6"/>
        <rect x="4" y="32" width="52" height="44" rx="2" fill="#fff"/>
        <circle cx="30" cy="50" r="5" fill="var(--brand-red)"/>
        <rect x="27.5" y="52" width="5" height="10" fill="var(--brand-red)"/>
      </svg>
      <p class="feature-label">Antivirus &amp;<br>Antimalware<br>Protection</p>
    </div>
    <div class="feature" style="left:216px">
      <svg viewBox="0 0 72 72" width="70" aria-hidden="true">
        <path d="M2 2 H52 M2 2 V60" stroke="#fff" stroke-width="3" fill="none"/>
        <path d="M9 8 H58 M9 8 V66" stroke="#fff" stroke-width="3" fill="none"/>
        <path d="M16 14 H70 V50 L54 68 H16 Z" fill="none" stroke="#fff" stroke-width="4"/>
        <path d="M54 68 V50 H70" fill="#fff"/>
        <path d="M26 28 H60 M26 36 H60 M26 44 H52 M26 52 H46" stroke="#fff" stroke-width="3"/>
      </svg>
      <p class="feature-label">Data Back Up</p>
    </div>
    <div class="feature" style="left:426px">
      <svg viewBox="0 0 70 70" width="66" aria-hidden="true">
        <path d="M10 42 A26 26 0 0 1 52 13" fill="none" stroke="#fff" stroke-width="5"/>
        <path d="M60 28 A26 26 0 0 1 18 57" fill="none" stroke="#fff" stroke-width="5"/>
        <path d="M44 4 L58 12 L46 22 Z" fill="#fff"/>
        <path d="M26 66 L12 58 L24 48 Z" fill="#fff"/>
        <path d="M23 36 L32 45 L48 26" fill="none" stroke="#fff" stroke-width="5"/>
      </svg>
      <p class="feature-label">Automatic<br>Update<br>Vantix<br>Desktop and<br>3rd Party<br>Software</p>
    </div>
    <div class="feature" style="left:637px">
      <svg viewBox="0 0 90 60" width="84" aria-hidden="true">
        <path d="M2 2 H70 M2 2 V48" stroke="#fff" stroke-width="4" fill="none"/>
        <path d="M10 10 H78 M10 10 V56" stroke="#fff" stroke-width="4" fill="none"/>
        <rect x="19" y="19" width="68" height="38" fill="none" stroke="#fff" stroke-width="5"/>
        <circle cx="53" cy="38" r="10" fill="#fff"/>
        <text x="53" y="43" text-anchor="middle" font-family="Lato, sans-serif" font-weight="900" font-size="14" fill="var(--brand-red)">$</text>
      </svg>
      <p class="feature-label">Discounted<br>Rates for On<br>Site or Remote<br>Service Calls</p>
    </div>
  </section>

  <aside class="testimonial">
    <p>Your company is the greatest. I can’t imagine living without you!<br>-Satisfied Customer</p>
    <p>Lorem ipsum dolor sit amet, consectetuer adipiscing elit. Aenean commodo ligula eget dolor. Aenean massa. Cum sociis natoque penatibus et magnis dis parturient montes, nascetur ridiculus mus.<br>-Satisfied Customer</p>
  </aside>
  <svg class="testimonial-tail" width="160" height="84" viewBox="0 0 160 84" aria-hidden="true">
    <path d="M17 0 H156 L1 84 Z" fill="var(--quote-bg)"/>
  </svg>

  <section class="pitch">
    <p>At Bright Owl Support, we have years of experience protecting the computers and networks of our commercial business clients.</p>
    <p>Now, we are making the same Enterprise Grade security and protection available to our home users for a flat monthly rate.</p>
    <p>It’s like having your own personal IT department!</p>
  </section>

  <p class="cta"><span class="cta-lead">SIGN UP TODAY</span> and get a free tutoring session to learn the inside security secrets the pros use!</p>

  <footer class="contact">www.brightowlsupport.example &nbsp;|&nbsp; 555-014-2290</footer>
</main>
</body>
</html>
```